Website needed for Entertainment Company [Wordpress & Mobile Site] (Contest)

"Vault Learning" does Acrobatic Educational Shows for schools.
We need a 4-Page Wordpress site, for BOTH Desktop & Mobile
THINGS WE'D LIKE ON THE HOME PAGE
- Book Now buttons
- Panel advertising "Kindness-First Tumbling Tour" with subheading "Educating the Victim, Empowering the Bystander, and Enlightening the Bully" with Photo & 'Read More'
- text somewhere saying "Vault Learning engages children in important topics, by utilising Parkour & Acrobatics to captivate and enthrall todays youngest generation."
- Panel advertising Teachers Resources: "Curriculum based resources for teachers including lesson plans, workbooks, and physical activities for before & after the show." Maybe even some boxes that say a subject that is covered (eg. Mathematics. Science. PD/H/PE.)
- Everything else that you recommend
4 PAGES:
- Home Page
- About Us
- Our Program & Shows
- Teachers Resources Portal
NOTE: Transparent & Source files for logo will be provided soon (recently finished being designed)

```html
<!DOCTYPE html>
<html lang="en">
<head>
<meta charset="utf-8">
<title>Vault Learning</title>
<link href="https://fonts.googleapis.com/css2?family=Montserrat:wght@500;600;700&family=Open+Sans:wght@400;600&display=swap" rel="stylesheet">
<style>
:root{
  --blue:#2467a1;
  --blue-dark:#1f5a8e;
  --orange:#d9532c;
  --orange-btn:#d9442a;
  --ink:#1d1d1d;
  --text:#333;
  --green:#3daa4a;
  --star:#f5a623;
  --grey:#f4f4f4;
  --box-border:#7a7a7a;
}
*{box-sizing:border-box;margin:0;padding:0}
html,body{width:1200px;height:3689px;overflow:hidden}
body{position:relative;font-family:"Open Sans",Arial,sans-serif;color:var(--text);background:#fff}
.abs{position:absolute}
.center{left:0;width:1200px;text-align:center}
.heading{font-family:"Montserrat",Arial,sans-serif;font-weight:700;color:var(--ink)}
.btn{position:absolute;display:flex;align-items:center;justify-content:center;border:2px solid var(--orange-btn);border-radius:4px;color:var(--ink);font-size:18px;background:#fff}
.btn-sm{font-size:15px;height:34px;width:124px}

/* header */
.brand{position:absolute;display:flex;align-items:center;gap:14px;font-family:"Montserrat",sans-serif;font-weight:700;color:var(--orange);font-size:36px}
.brand-dot{width:34px;height:34px;border-radius:50%;background:var(--orange)}
.contact-top{position:absolute;top:58px;font-size:16px;color:#444;display:flex;align-items:center;gap:10px}
.nav{position:absolute;top:133px;left:0;width:1200px;height:72px;background:var(--blue);display:flex;justify-content:center;gap:50px;align-items:center}
.nav a{color:#fff;font-family:"Montserrat",sans-serif;font-weight:600;font-size:16px;text-decoration:none}

/* hero */
.hero{position:absolute;top:205px;left:0;width:1200px;height:580px}
.hero-title{position:absolute;top:145px;left:0;width:1200px;text-align:center;color:#fff;font-family:"Montserrat",sans-serif;font-weight:700;font-size:56px;line-height:64px}
.hero .btn{background:transparent;color:#fff;left:518px;top:292px;width:165px;height:46px;font-size:19px}

/* about */
.about-p{position:absolute;left:205px;width:790px;top:966px;text-align:center;font-size:16px;line-height:27px}

/* show */
.show{position:absolute;top:1212px;left:0;width:1200px;height:554px;background:var(--orange)}
.show-title{top:56px;color:#fff;font-size:38px}
.card{position:absolute;top:147px;width:289px;height:357px;background:#fff}
.card-img{height:192px;width:100%}
.card-label{position:absolute;top:178px;left:22px;width:245px;height:28px;background:var(--blue);color:#fff;font-family:"Montserrat",sans-serif;font-weight:700;font-size:16px;text-align:center;line-height:28px}
.card-text{position:absolute;top:224px;left:10px;width:269px;text-align:center;font-size:15.5px;line-height:19px}
.card .btn{top:304px;left:82px}

/* quote */
.quote{position:absolute;top:1766px;left:0;width:1200px;height:270px;background:var(--blue)}
.quote p{position:absolute;top:68px;left:0;width:1200px;text-align:center;color:#fff;font-family:"Montserrat",sans-serif;font-weight:700;font-size:21.5px;line-height:36px}
.quote .btn{background:transparent;border-color:#fff;color:#fff;left:505px;top:164px;width:164px;height:47px;font-size:19px}

/* resources */
.res{position:absolute;width:288px;height:253px;border:2.5px solid var(--box-border);background:#fff;text-align:center}
.res-icon{position:absolute;left:116px;top:14px;width:56px;height:56px;border-radius:6px;background:var(--orange);opacity:.85}
.res h3{position:absolute;top:86px;left:0;width:100%;font-family:"Montserrat",sans-serif;font-weight:600;font-size:18px;color:var(--ink)}
.res p{position:absolute;top:114px;left:20px;width:244px;font-size:15.5px;line-height:19px}
.res .btn{top:188px;left:75px;width:140px;height:38px;font-size:16px}

/* testimonial */
.testi{position:absolute;top:2858px;left:0;width:1200px;height:432px;background:linear-gradient(180deg,#2e5f93,#3f73a8 60%,#2c5b8c)}
.testi-card{position:absolute;top:74px;left:210px;width:781px;height:272px;background:#fff}
.avatar{position:absolute;top:30px;left:556px;width:88px;height:88px;border-radius:50%;background:var(--green)}
.arrow{position:absolute;top:210px;width:50px;height:50px;border-radius:50%;background:#fff}

/* footer */
.footer{position:absolute;top:3290px;left:0;width:1200px;height:399px;background:#fff}
.footer h4{position:absolute;font-family:"Montserrat",sans-serif;font-weight:600;font-size:19px;color:var(--ink)}
.flinks{position:absolute;left:536px;top:138px;font-size:15.5px;line-height:34px;color:#333}
.fcontact{position:absolute;left:795px;top:140px;font-size:15.5px;line-height:32px;color:#333}
.fcontact div{display:flex;align-items:center;gap:10px}
.social{position:absolute;top:350px;width:16px;height:16px;border-radius:50%;background:#222}
</style>
</head>
<body>

<header>
  <div class="brand" style="left:100px;top:52px"><span class="brand-dot"></span>Vault Learning</div>
  <div class="contact-top" style="left:646px">
    <svg width="24" height="24" viewBox="0 0 24 24" fill="none" stroke="#6b9bc9" stroke-width="1.6"><path d="M5 3h4l2 5-2.5 1.5a11 11 0 0 0 6 6L16 13l5 2v4a2 2 0 0 1-2 2A16 16 0 0 1 3 5a2 2 0 0 1 2-2z"/></svg>
    1300 482 610
  </div>
  <div class="contact-top" style="left:822px;top:56px">
    <svg width="22" height="16" viewBox="0 0 22 16" fill="none" stroke="#6b9bc9" stroke-width="1.5"><rect x="1" y="1" width="20" height="14"/><path d="M1 1l10 8 10-8"/></svg>
    hello@vaultlearning.example
  </div>
  <nav class="nav">
    <a href="#">Home</a><a href="#">About Us</a><a href="#">Program &amp; Shows</a><a href="#">Teachers Resources Portal</a><a href="#">Contact Us</a>
  </nav>
</header>

<section class="hero">
  <svg class="abs" style="left:0;top:0" width="1200" height="580" role="img" aria-label="Photo of a coach guiding young gymnasts stretching in a school hall">
    <defs><linearGradient id="heroG" x1="0" y1="0" x2="1" y2="1"><stop offset="0" stop-color="#8a6a4a"/><stop offset=".5" stop-color="#6e5a55"/><stop offset="1" stop-color="#5a5d66"/></linearGradient></defs>
    <polygon points="0,0 1200,0 1200,580 0,490" fill="url(#heroG)"/>
    <polygon points="0,0 1200,0 1200,580 0,490" fill="#000" opacity=".25"/>
  </svg>
  <h1 class="hero-title">Acrobatic Educational Shows<br>for schools.</h1>
  <a class="btn" href="#">Book Now</a>
</section>

<section>
  <div class="abs" style="left:557px;top:797px;width:86px;height:86px;border-radius:50%;background:var(--blue)"></div>
  <h2 class="abs center heading" style="top:886px;font-size:37px">Vault Learning</h2>
  <p class="about-p">Vault Learning Productions is all about experiences. Our company was built on the principle that we create our understanding of the world out first from our experiences, and throughout our lives this remains the most effective and convincing way we learn. We constantly strive to inspire, astound, teach, and encapture our clients and audiences in unique ways</p>
  <a class="btn" href="#" style="left:518px;top:1109px;width:165px;height:45px">Read More</a>
</section>

<section class="show">
  <h2 class="abs center heading show-title">Kindness-First Tumbling Tour</h2>
  <div class="card" style="left:127px">
    <div class="card-img" role="img" aria-label="Photo of a student sitting alone against a brick wall" style="background:linear-gradient(135deg,#8c8f95,#5b6b80)"></div>
    <div class="card-label">Educating the Victim</div>
    <p class="card-text">Lorem Ipsum is simply dummy text of the printing and typesetting industry.</p>
    <a class="btn btn-sm" href="#">Read More</a>
  </div>
  <div class="card" style="left:457px">
    <div class="card-img" role="img" aria-label="Photo of a performer leaping in front of seated students" style="background:linear-gradient(135deg,#e4e4e4,#9a9a9a)"></div>
    <div class="card-label">Empowering the Bystander</div>
    <p class="card-text">Lorem Ipsum is simply dummy text of the printing and typesetting industry.</p>
    <a class="btn btn-sm" href="#">Read More</a>
  </div>
  <div class="card" style="left:784px">
    <div class="card-img" role="img" aria-label="Photo of an aerial hoop performer on a lit stage" style="background:linear-gradient(135deg,#1b2570,#3b47a8)"></div>
    <div class="card-label">Enlightening the Bully</div>
    <p class="card-text">Lorem Ipsum is simply dummy text of the printing and typesetting industry.</p>
    <a class="btn btn-sm" href="#">Read More</a>
  </div>
</section>

<section class="quote">
  <p>"Vault Learning engages children in important topics, by utilising Parkour &amp; Acrobatics<br>to captivate and enthrall todays youngest generation."</p>
  <a class="btn" href="#">Click Here</a>
</section>

<section>
  <h2 class="abs center heading" style="top:2094px;font-size:37px">Teachers Resources</h2>
  <p class="abs center" style="top:2155px;font-size:17px">Curriculum based resources for teachers including:</p>

  <div class="res" style="left:136px;top:2237px"><div class="res-icon" role="img" aria-label="Lesson plans icon"></div><h3>Lesson Plans</h3><p>Lorem Ipsum is simply dummy text of the printing and typesetting industry</p><a class="btn" href="#">Read More</a></div>
  <div class="res" style="left:458px;top:2237px"><div class="res-icon" role="img" aria-label="Workbooks icon"></div><h3>Workbooks</h3><p>Lorem Ipsum is simply dummy text of the printing and typesetting industry</p><a class="btn" href="#">Read More</a></div>
  <div class="res" style="left:780px;top:2237px"><div class="res-icon" role="img" aria-label="Physical activities icon"></div><h3>Physical Activities</h3><p>Lorem Ipsum is simply dummy text of the printing and typesetting industry</p><a class="btn" href="#">Read More</a></div>
  <div class="res" style="left:133px;top:2537px"><div class="res-icon" role="img" aria-label="Mathematics icon"></div><h3>Mathematics</h3><p>Lorem Ipsum is simply dummy text of the printing and typesetting industry</p><a class="btn" href="#">Read More</a></div>
  <div class="res" style="left:455px;top:2537px"><div class="res-icon" role="img" aria-label="Science icon"></div><h3>Science</h3><p>Lorem Ipsum is simply dummy text of the printing and typesetting industry</p><a class="btn" href="#">Read More</a></div>
  <div class="res" style="left:777px;top:2537px"><div class="res-icon" role="img" aria-label="PD/H/PE icon"></div><h3>PD/H/PE</h3><p>Lorem Ipsum is simply dummy text of the printing and typesetting industry</p><a class="btn" href="#">Read More</a></div>
</section>

<section class="testi" role="img" aria-label="Faded photo of children performing gymnastics behind the testimonial">
  <div class="testi-card">
    <div class="abs" style="top:78px;left:0;width:781px;text-align:center;color:var(--star);font-size:24px;letter-spacing:2px">★★★★★</div>
    <p class="abs" style="top:128px;left:60px;width:661px;text-align:center;font-size:15.5px;line-height:27px"><b style="font-size:28px;line-height:0">“</b>Lorem Ipsum is simply dummy text of the printing and typesetting industry. Lorem Ipsum has been the industry's standard dummy text.<b style="font-size:28px;line-height:0">”</b></p>
    <p class="abs" style="top:196px;left:0;width:781px;text-align:center;font-weight:600;font-size:15px">-MARCUS</p>
  </div>
  <div class="avatar">
    <svg width="88" height="88" viewBox="0 0 88 88"><circle cx="44" cy="36" r="11" fill="#fff"/><path d="M25 62a19 14 0 0 1 38 0z" fill="#fff"/></svg>
  </div>
  <div class="arrow" style="left:115px"><svg width="50" height="50"><path d="M29 15L19 25l10 10" stroke="var(--blue)" stroke-width="4" fill="none"/></svg></div>
  <div class="arrow" style="left:1016px"><svg width="50" height="50"><path d="M21 15l10 10-10 10" stroke="var(--blue)" stroke-width="4" fill="none"/></svg></div>
</section>

<footer class="footer">
  <div class="brand" style="left:118px;top:160px"><span class="brand-dot"></span>Vault Learning</div>
  <h4 style="left:535px;top:96px">Quick Links</h4>
  <div class="flinks">Home<br>About Us<br>Program &amp; Shows<br>Teachers Resources Portal<br>Contact Us</div>
  <h4 style="left:795px;top:94px">Contact us</h4>
  <div class="fcontact">
    <div><svg width="16" height="20" viewBox="0 0 16 20"><path d="M8 0a7 7 0 0 0-7 7c0 5 7 13 7 13s7-8 7-13a7 7 0 0 0-7-7z" fill="#111"/><circle cx="8" cy="7" r="2.5" fill="#fff"/></svg>17 Harbour Lane</div>
    <div style="padding-left:26px">Brookvale, NSW 2100</div>
    <div><svg width="16" height="16" viewBox="0 0 24 24"><path d="M5 2h4l2 5-2.5 1.5a11 11 0 0 0 6 6L16 12l5 2v4a2 2 0 0 1-2 2A17 17 0 0 1 3 4a2 2 0 0 1 2-2z" fill="#111"/></svg>+1300 482 610</div>
    <div style="margin-top:6px"><svg width="18" height="14" viewBox="0 0 18 14" fill="none" stroke="#111" stroke-width="1.5"><rect x="1" y="1" width="16" height="12"/><path d="M1 1l8 7 8-7"/></svg>hello@vaultlearning.example</div>
  </div>
  <p class="abs" style="left:95px;top:355px;font-size:17px;color:#333">Copyright © Vault Learning</p>
  <span class="social" style="left:1030px"></span>
  <span class="social" style="left:1058px"></span>
  <span class="social" style="left:1086px"></span>
</footer>

</body>
</html>
```